PELDRAX Business Cards

We require a business card for our company that provides IT consulting services. We already have a logo that needs to be used on the card. We want a clean professional looking design that incorporates our colours. Our main focus is providing managed services to business, which involves us looking after all of their IT requirements including managing servers/networks, projects, and procurement.

Industry/Entity Type

Information Technology

Requirements
Must have
• our logo, contact information, name, title, phone numbers

```html
<!DOCTYPE html>
<html lang="en">
<head>
<meta charset="utf-8">
<title>PELDRAX Business Cards</title>
<link href="https://fonts.googleapis.com/css2?family=Lato:wght@400;700;900&family=Arimo:wght@400&display=swap" rel="stylesheet">
<style>
  :root {
    --backdrop: #1c1c1c;
    --card-white: #f7f7f7;
    --brand-blue: #0a92cf;
    --tab-blue: #24a6e0;
    --tab-light: #7fcdf2;
    --ink: #333333;
    --rule-grey: #b9bcbf;
    --white: #ffffff;
  }
  html, body {
    margin: 0;
    padding: 0;
    width: 900px;
    height: 1200px;
    overflow: hidden;
    background: var(--backdrop);
  }
  .canvas {
    position: relative;
    width: 900px;
    height: 1200px;
  }
  .card {
    position: absolute;
    left: 87px;
    width: 733px;
    height: 429px;
    border-radius: 24px;
    overflow: hidden;
    box-shadow: 0 6px 14px rgba(0,0,0,0.55);
  }
  /* Front */
  .card-front {
    top: 126px;
    background: radial-gradient(ellipse at 75% 40%, #ffffff 0%, var(--card-white) 55%, #ececec 100%);
  }
  .brand-name {
    position: absolute;
    font-family: "Lato", sans-serif;
    font-weight: 900;
    letter-spacing: 2px;
    margin: 0;
  }
  .card-front .brand-name {
    left: 52px;
    top: 82px;
    font-size: 44px;
    color: var(--brand-blue);
    display: flex;
    align-items: center;
    gap: 14px;
  }
  .brand-dot {
    width: 30px;
    height: 30px;
    border-radius: 50%;
    background: currentColor;
    display: inline-block;
  }
  .name-tab {
    position: absolute;
    left: 435px;
    top: 79px;
    width: 248px;
    height: 30px;
    background: var(--tab-blue);
    border-radius: 0 8px 0 8px;
    color: var(--white);
    font-family: "Lato", sans-serif;
    font-weight: 900;
    font-size: 24px;
    letter-spacing: 1.5px;
    text-align: right;
    padding-right: 14px;
    box-sizing: border-box;
    line-height: 31px;
  }
  .title-tab {
    position: absolute;
    left: 464px;
    top: 112px;
    width: 219px;
    height: 27px;
    background: var(--tab-light);
    border-radius: 0 8px 0 8px;
    color: var(--white);
    font-family: "Lato", sans-serif;
    font-weight: 700;
    font-size: 17px;
    letter-spacing: 0.6px;
    text-align: right;
    padding-right: 12px;
    box-sizing: border-box;
    line-height: 28px;
  }
  .edge-tab {
    position: absolute;
    left: 709px;
    width: 30px;
    border-radius: 8px 0 0 8px;
  }
  .edge-tab.dark { top: 79px; height: 30px; background: var(--tab-blue); }
  .edge-tab.light { top: 112px; height: 27px; background: var(--tab-light); }
  .contact-list {
    position: absolute;
    left: 47px;
    top: 255px;
    margin: 0;
    padding: 0;
    list-style: none;
    font-family: "Arimo", sans-serif;
    font-size: 16.5px;
    color: var(--ink);
  }
  .contact-list li {
    display: flex;
    align-items: center;
    height: 25.5px;
  }
  .contact-list svg {
    width: 16px;
    height: 16px;
    margin-right: 11px;
    fill: var(--brand-blue);
  }
  .address {
    position: absolute;
    right: 49px;
    top: 308px;
    margin: 0;
    text-align: right;
    font-family: "Arimo", sans-serif;
    font-style: normal;
    font-size: 16.5px;
    line-height: 25px;
    color: var(--ink);
  }
  .rule {
    position: absolute;
    left: 0;
    top: 390px;
    width: 100%;
    height: 3px;
    background: var(--rule-grey);
  }
  .web-band {
    position: absolute;
    left: 0;
    top: 395px;
    width: 100%;
    height: 34px;
    background: var(--brand-blue);
    color: var(--white);
    font-family: "Lato", sans-serif;
    font-weight: 900;
    font-size: 15px;
    letter-spacing: 1.5px;
    text-align: center;
    line-height: 34px;
  }
  /* Back */
  .card-back {
    top: 640px;
    background: radial-gradient(circle at 88% 12%, #2aa8e4 0%, #1b9ad8 35%, var(--brand-blue) 70%, #0789c6 100%);
  }
  .card-back .brand-name {
    left: 0;
    width: 100%;
    top: 188px;
    font-size: 52px;
    color: var(--white);
    display: flex;
    justify-content: center;
    align-items: center;
    gap: 16px;
  }
  .card-back .brand-dot { width: 36px; height: 36px; }
  .back-web {
    position: absolute;
    left: 0;
    width: 100%;
    top: 372px;
    text-align: center;
    color: var(--white);
    font-family: "Lato", sans-serif;
    font-size: 17px;
    letter-spacing: 1.5px;
  }
  .back-web strong { font-weight: 900; }
</style>
</head>
<body>
<main class="canvas">
  <section class="card card-front" aria-label="Business card front">
    <h1 class="brand-name"><span class="brand-dot"></span>PELDRAX</h1>
    <div class="name-tab">MARTEN HOLLIS</div>
    <div class="title-tab">MANAGING DIRECTOR</div>
    <div class="edge-tab dark"></div>
    <div class="edge-tab light"></div>

    <ul class="contact-list">
      <li>
        <svg viewBox="0 0 16 16" aria-hidden="true"><path d="M4 0h8a1 1 0 0 1 1 1v14a1 1 0 0 1-1 1H4a1 1 0 0 1-1-1V1a1 1 0 0 1 1-1zm1 2v5h6V2zm0 7v1.5h1.5V9zm2.2 0v1.5h1.6V9zm2.3 0v1.5H11V9zM5 11.5V13h1.5v-1.5zm2.2 0V13h1.6v-1.5zm2.3 0V13H11v-1.5z"/></svg>
        555.310.0482
      </li>
      <li>
        <svg viewBox="0 0 16 16" aria-hidden="true"><path d="M3.6 1.2l2.3 2.3c.4.4.4 1 0 1.4L4.7 6.1c.9 2 2.6 3.7 4.6 4.6l1.2-1.2c.4-.4 1-.4 1.4 0l2.3 2.3c.4.4.4 1 0 1.4l-1.3 1.3c-.6.6-1.5.8-2.3.5C6.3 13.5 2.5 9.7 1 5.4c-.3-.8-.1-1.7.5-2.3l1.3-1.3c.3-.4.4-.5.8-.6z"/></svg>
        555.310.0490
      </li>
      <li>
        <svg viewBox="0 0 16 16" aria-hidden="true"><path d="M4 1h8v4H4zM1 6h14v6h-3v-2H4v2H1zm4 5h6v4H5z"/></svg>
        555.720.1166
      </li>
      <li>
        <svg viewBox="0 0 16 16" aria-hidden="true"><path d="M1 3h14v10H1zm1.5 1.3v.4L8 9l5.5-4.3v-.4zm0 2.2v5.2l3.4-2.6zm11 0L10.1 9.1l3.4 2.6z"/></svg>
        marten@peldrax.com
      </li>
    </ul>

    <address class="address">278 Linden Crescent<br>Fairmont, California 94018</address>

    <div class="rule"></div>
    <div class="web-band">WWW.PELDRAX.COM</div>
  </section>

  <section class="card card-back" aria-label="Business card back">
    <p class="brand-name"><span class="brand-dot"></span>PELDRAX</p>
    <p class="back-web">WWW.<strong>PELDRAX</strong>.COM</p>
  </section>
</main>
</body>
</html>
```